Business cards for Champion Suri Alpaca Breeder

I am a seed stock Suri Alpaca breeder. I am looking for a business card design that is tactile with my logo or part of my logo embossed or debossed. I am open to other ideas.
My logo is available in detailed and simplified version. To get a feel for my style visit my website fernwoodgrazerherd.com

Target Market(s)

Alpaca breeders

Industry/Entity Type

Alpaca / Livestock

Contact Information for Business Card

Logo, Molly Ferris, FERNWOODgrazer.com, Saint Louis, MO 314-527-9160

Colors
0054AA
0677BA
7BADD7
CADEEF
E8F1F8

Requirements
Must have
• use brand guide
Nice to have
• embossed or debossed, incorporating a simple plaid use complimentary colors in logo
Should not have
• cartoon alpacas

```html
<!DOCTYPE html>
<html lang="en">
<head>
<meta charset="utf-8">
<title>Fernwood &amp; Co — Business Cards</title>
<link href="https://fonts.googleapis.com/css2?family=Crimson+Text:wght@400;600&family=Allura&display=swap" rel="stylesheet">
<style>
  :root {
    --stage: #e9e9e7;
    --card-grey: #d8d7d3;
    --card-white: #fbfbfa;
    --ink-navy: #1f2a3c;
    --ink-dark: #2b2b2b;
    --ink-soft: #5a5a5a;
    --rule-gold: #c9b79a;
    --faint-mark: #ececea;
  }
  * { box-sizing: border-box; margin: 0; padding: 0; }
  html, body { width: 1200px; height: 900px; overflow: hidden; }
  body {
    background: var(--stage);
    position: relative;
    font-family: "Crimson Text", Georgia, serif;
    color: var(--ink-dark);
  }
  .card {
    position: absolute;
    width: 620px;
    height: 354px;
    box-shadow: 0 10px 28px rgba(0,0,0,0.18);
    overflow: hidden;
  }

  /* Logo side */
  .card--brand {
    left: 150px; top: 70px;
    background: var(--card-grey);
  }
  .brand-mark {
    position: absolute;
    left: 0; right: 0; top: 112px;
    display: flex; align-items: center; justify-content: center; gap: 14px;
  }
  .brand-mark__dot {
    width: 16px; height: 16px; border-radius: 50%;
    background: var(--ink-navy);
  }
  .brand-mark__name {
    font-size: 40px; font-weight: 400; letter-spacing: 3px;
    color: var(--ink-navy);
  }
  .brand-rule {
    position: absolute; left: 90px; right: 90px; top: 214px;
    height: 1.5px; background: var(--ink-navy);
  }
  .brand-url {
    position: absolute; left: 0; right: 0; top: 236px;
    text-align: center;
    font-size: 20px; letter-spacing: 8px;
    color: var(--ink-navy);
  }

  /* Contact side */
  .card--contact {
    left: 430px; top: 476px;
    background: var(--card-white);
  }
  .faint-mark {
    position: absolute; left: 30px; top: 20px;
    width: 300px; height: 300px; border-radius: 50%;
    background: var(--faint-mark);
  }
  .contact-logo {
    position: absolute; right: 40px; top: 50px;
    width: 250px; text-align: center;
  }
  .contact-logo__row {
    display: flex; align-items: center; justify-content: center; gap: 10px;
  }
  .contact-logo__dot {
    width: 12px; height: 12px; border-radius: 50%;
    background: var(--ink-dark);
  }
  .contact-logo__name {
    font-size: 30px; letter-spacing: 1px; color: var(--ink-dark);
  }
  .contact-logo__rule {
    margin: 18px auto 0; width: 220px; height: 1px;
    background: var(--rule-gold);
  }
  .contact-name {
    position: absolute; left: 48px; top: 196px;
    font-family: "Allura", cursive;
    font-size: 42px; color: var(--ink-navy);
  }
  .contact-list {
    position: absolute; left: 50px; top: 262px;
    list-style: none;
    font-size: 18px; color: var(--ink-soft); line-height: 28px;
  }
  .contact-list li, .contact-address {
    display: flex; align-items: flex-start; gap: 10px;
  }
  .icon { width: 14px; height: 16px; margin-top: 6px; flex: none; }
  .contact-address {
    position: absolute; left: 300px; top: 230px;
    font-size: 18px; color: var(--ink-soft); line-height: 26px;
  }
</style>
</head>
<body>

<section class="card card--brand">
  <div class="brand-mark">
    <span class="brand-mark__dot"></span>
    <span class="brand-mark__name">FERNWOOD &amp; CO</span>
  </div>
  <div class="brand-rule"></div>
  <p class="brand-url">FERNWOODgrazer.com</p>
</section>

<section class="card card--contact">
  <div class="faint-mark"></div>

  <div class="contact-logo">
    <div class="contact-logo__row">
      <span class="contact-logo__dot"></span>
      <span class="contact-logo__name">FERNWOOD &amp; CO</span>
    </div>
    <div class="contact-logo__rule"></div>
  </div>

  <p class="contact-name">Molly Ferris</p>

  <ul class="contact-list">
    <li>
      <svg class="icon" viewBox="0 0 14 16" aria-hidden="true">
        <rect x="3" y="0.8" width="8" height="14.4" rx="1.5" fill="none" stroke="#5a5a5a" stroke-width="1.4"/>
        <line x1="6" y1="12.8" x2="8" y2="12.8" stroke="#5a5a5a" stroke-width="1.4"/>
      </svg>
      <span>314-527-9160</span>
    </li>
    <li>
      <svg class="icon" viewBox="0 0 14 16" aria-hidden="true">
        <circle cx="7" cy="8" r="6" fill="none" stroke="#1f2a3c" stroke-width="1.6"/>
        <path d="M1 8h12M7 2c-2.5 3-2.5 9 0 12M7 2c2.5 3 2.5 9 0 12" fill="none" stroke="#1f2a3c" stroke-width="1"/>
      </svg>
      <span>FERNWOODgrazer.com</span>
    </li>
  </ul>

  <div class="contact-address">
    <svg class="icon" viewBox="0 0 14 16" aria-hidden="true">
      <path d="M7 15.5C7 15.5 1.5 9.5 1.5 6a5.5 5.5 0 0 1 11 0c0 3.5-5.5 9.5-5.5 9.5z" fill="none" stroke="#1f2a3c" stroke-width="1.6"/>
      <circle cx="7" cy="6" r="2" fill="#1f2a3c"/>
    </svg>
    <span>Willow Bend Farm<br>Cedar Hollow, MO</span>
  </div>
</section>

</body>
</html>
```